business card design for a small scale specialty cut flower farm

We need a business card design for Hollowmere Bloom Farm based in Langley, BC, Canada. We produce specialty, high-end cut flowers and sell locally to florists, local shops and markets and the end user through bouquet subscriptions. The final business card design should be memorable and have a timeless or vintage feel. We would prefer a square shape.
Updates

Target Market(s)

florists, shops and seasonal markets, local flower lovers

Industry/Entity Type

Floral

Contact Information for Business Card

Tamsin Ellery Voss, Grower
Langley, BC, Canada
website: hollowmerebloomfarm.example
instagram: @hollowmerebloomfarm
Tel: 555.317.4290
facebook: www.facebook.example/hollowmereblooms/

Font styles to use
Serif
Decorative
Script

Requirements
Must have
• soft black background colour on front side, the included logo and catch phrase: Fresh Local Seasonal
Nice to have
• phone number and website address on front of card, included photo 6539 incorporated onto the back, possibly photo 6609 as well.

```html
<!DOCTYPE html>
<html lang="en">
<head>
<meta charset="utf-8">
<title>Hollowmere Bloom Farm – Business Card</title>
<link rel="stylesheet" href="https://fonts.googleapis.com/css2?family=Montserrat:wght@400;500&family=Open+Sans:wght@400;700&display=swap">
<style>
  :root {
    --canvas: #e6e6e8;
    --soft-black: #242324;
    --paper-light: #f3f1ee;
    --paper-muted: #c9c6c2;
    --ink: #1f1f1f;
    --ink-soft: #3a3a3a;
    --wall-pink: #d0476f;
    --wall-pink-deep: #b8355c;
    --delphinium: #5a3fc9;
    --dahlia-red: #c8334f;
    --dahlia-wine: #7a1a3c;
    --bucket-blue: #b9cde0;
    --bucket-pale: #dbe6ef;
    --band-olive: #a2a932;
    --logo-rose: #f2a9c7;
  }
  * { box-sizing: border-box; margin: 0; padding: 0; }
  html, body { width: 1200px; height: 800px; overflow: hidden; }
  body {
    background: var(--canvas);
    position: relative;
    font-family: "Montserrat", sans-serif;
    color: var(--ink);
  }
  .card {
    position: absolute;
    top: 160px;
    width: 480px;
    height: 480px;
    border-radius: 3px;
    box-shadow: 0 10px 28px rgba(0,0,0,0.18);
    overflow: hidden;
  }

  /* Photo side */
  .card--photo { left: 90px; }
  .photo-fill {
    position: absolute; inset: 0;
    background:
      radial-gradient(ellipse 36% 22% at 52% 20%, var(--delphinium) 0%, rgba(90,63,201,0) 100%),
      radial-gradient(ellipse 28% 20% at 18% 38%, #e2458f 0%, rgba(226,69,143,0) 100%),
      radial-gradient(ellipse 24% 16% at 74% 50%, #e2c23a 0%, rgba(226,194,58,0) 100%),
      radial-gradient(ellipse 42% 26% at 44% 58%, var(--dahlia-red) 0%, var(--dahlia-wine) 55%, rgba(122,26,60,0) 100%),
      linear-gradient(180deg, rgba(185,205,224,0) 62%, var(--bucket-blue) 74%, var(--bucket-pale) 100%),
      linear-gradient(90deg, var(--wall-pink-deep), var(--wall-pink));
  }
  .person {
    position: absolute; top: 32px; right: 30px;
    text-align: right;
    font-family: "Open Sans", sans-serif;
  }
  .person__name { font-weight: 700; font-size: 22px; color: var(--ink); }
  .person__role { font-weight: 400; font-size: 15px; color: var(--ink-soft); margin-top: 2px; }
  .tagline-band {
    position: absolute; left: 0; right: 0; bottom: 44px; height: 36px;
    background: var(--band-olive);
    display: flex; align-items: center; padding-left: 30px;
    font-weight: 500; font-size: 15px; letter-spacing: 0.32em; color: var(--ink);
  }

  /* Logo and contact side */
  .card--contact {
    left: 630px;
    background: var(--soft-black);
    color: var(--paper-light);
    display: flex; flex-direction: column; align-items: center;
  }
  .brand { margin-top: 150px; display: flex; align-items: center; gap: 14px; }
  .brand__mark { width: 30px; height: 30px; border-radius: 50%; background: var(--logo-rose); }
  .brand__name { font-weight: 500; font-size: 26px; letter-spacing: 0.04em; color: var(--paper-light); }
  .contact { margin-top: 110px; text-align: center; font-size: 15px; line-height: 1.6; color: var(--paper-light); }
  .contact__row { display: flex; align-items: center; justify-content: center; gap: 16px; }
  .contact__item { display: inline-flex; align-items: center; gap: 6px; }
  .contact__dot { width: 13px; height: 13px; border-radius: 50%; background: var(--paper-light); }
</style>
</head>
<body>
  <section class="card card--photo">
    <div class="photo-fill" role="img" aria-label="Photo of dahlias, delphiniums and hydrangeas in pale blue buckets against a pink wall"></div>
    <div class="person">
      <p class="person__name">Tamsin Ellery Voss</p>
      <p class="person__role">Grower</p>
    </div>
    <div class="tagline-band">FRESH LOCAL SEASONAL</div>
  </section>

  <section class="card card--contact">
    <div class="brand">
      <span class="brand__mark"></span>
      <span class="brand__name">Hollowmere Bloom Farm</span>
    </div>
    <div class="contact">
      <div class="contact__row">
        <span class="contact__item">
          <svg width="14" height="14" viewBox="0 0 24 24" aria-hidden="true"><path fill="#f3f1ee" d="M6.6 10.8a15.1 15.1 0 0 0 6.6 6.6l2.2-2.2c.3-.3.7-.4 1-.2 1.1.4 2.3.6 3.6.6.6 0 1 .4 1 1V20c0 .6-.4 1-1 1A17 17 0 0 1 3 4c0-.6.4-1 1-1h3.5c.6 0 1 .4 1 1 0 1.3.2 2.5.6 3.6.1.3 0 .7-.2 1z"/></svg>
          (555) 317-4290
        </span>
        <span class="contact__item"><span class="contact__dot"></span>@hollowmerebloomfarm</span>
      </div>
      <div class="contact__row">
        <span class="contact__item"><span class="contact__dot"></span>hollowmereblooms</span>
      </div>
      <p class="contact__web">www.hollowmerebloomfarm.example</p>
    </div>
  </section>
</body>
</html>
```